Plate Rally! Digital Order Web App

This is a web app on mobile phone, for consumers to order food inside a restaurant using their phones. we have done up the flow but we need to revamp UI design. pls have a look at our current web on your mobile phone:
https://demo.tavrozi.app/o/KLMV/314725

CURRENT DESIGN.
1. food category on left side, always shown. menu items in list view with image.
2. when we click on an item, there is popup page, to select modifiers, or quantity.
3. order review page(cart page) is quite messy now, need a complete new look.
4 payment page(no need to design, handle by Quellon)
5. order confirmation page. success or error return

DESIGN requirements:
please browse through and click to order with current page above. we have put in lots of thoughts and effort for current flow, the new design should base on this flow.
1. web app. no zoom in/out is allowed for users. responsive html to suit different mobile phone screen size. modern fonts.
2. PAGES needed:
home/welcome page,
well laid out menu items page,
single item page, with add on choice and modifier
cart page(to include recommended items, ordered item list, remove item total, changeable quantity,
confirmation page(success, fail)

DELIVERABLES - responsive html, fonts, images asset such as icons, animation, button images(suitable for commercial use without further third party loyalty fee)
Updates

Hi all if we have left a comment on ur design, please revise accordingly and we will conclude it soon!

Target Market(s)

young diners who order food on their mobile phone.

Industry/Entity Type

Restaurant

Coding

Coded - Design and coding required

Number of Pages Required

5+ page

Colors

Designer to choose colors to be used in the design.

Requirements
Must have
• - lively, appetising colors while making the page easy to read. easy on eyes.
• - consistency. fonts used.
Nice to have
• - 2 color schemes
• - html codes. we will top up if you can deliver coded html.
Should not have
• - should not have more than 3 colors
• - should not have more than 3 different fonts
• - should not use colors that are dull

```html
<!DOCTYPE html>
<html lang="en">
<head>
<meta charset="utf-8">
<title>Tavrozi – Vegetable Menu</title>
<link rel="stylesheet" href="https://fonts.googleapis.com/css2?family=Figtree:wght@400;500;600;700;800&family=Noto+Sans+SC:wght@400;500;700&display=swap">
<style>
  :root {
    --sidebar: #00bdd5;
    --main: #0098a6;
    --active: #0aa3b5;
    --white: #ffffff;
    --ink: #1b1b1b;
    --muted: #7a7a7a;
    --accent: #0098a6;
  }
  * { box-sizing: border-box; margin: 0; padding: 0; }
  html, body { width: 1200px; height: 904px; overflow: hidden; }
  body {
    font-family: "Figtree", "Noto Sans SC", sans-serif;
    background: var(--main);
    position: relative;
    color: var(--ink);
  }
  .sidebar {
    position: absolute; left: 0; top: 0; width: 336px; height: 904px;
    background: var(--sidebar);
  }
  .brand {
    position: absolute; left: 96px; top: 28px;
    color: var(--white); font-weight: 800; font-size: 36px; letter-spacing: 0.5px;
  }
  .category-nav { list-style: none; }
  .category-item {
    position: absolute; left: 96px; width: 240px; height: 56px;
    display: flex; align-items: center; gap: 18px; padding-left: 26px;
    color: var(--white); font-size: 23px; font-weight: 500;
  }
  .category-item svg { width: 26px; height: 26px; flex: none; }
  .category-item.is-active {
    background: var(--active); border-left: 2px solid var(--white); padding-left: 24px;
  }
  .page-title {
    position: absolute; left: 388px; top: 31px;
    color: var(--white); font-size: 30px; font-weight: 700;
  }
  .cart-button { position: absolute; left: 1120px; top: 36px; width: 40px; height: 32px; }
  .cart-badge {
    position: absolute; left: 1143px; top: 33px; width: 19px; height: 19px; border-radius: 50%;
    background: var(--white); color: var(--accent); font-size: 9px; font-weight: 700;
    display: flex; align-items: center; justify-content: center;
  }
  .dish-grid {
    position: absolute; left: 388px; top: 94px; width: 760px;
    display: grid; grid-template-columns: repeat(3, 236px); column-gap: 25px; row-gap: 26px;
  }
  .dish-card { width: 236px; height: 273px; background: var(--white); box-shadow: 0 4px 10px rgba(0,0,0,.12); }
  .dish-photo { height: 163px; border-radius: 0 62px 0 0; }
  .dish-info { position: relative; height: 110px; padding: 15px 17px 0; }
  .dish-name { font-size: 15.5px; font-weight: 700; line-height: 1.2; }
  .dish-sub { margin-top: 7px; font-size: 13.5px; color: var(--muted); font-weight: 500; }
  .dish-price {
    position: absolute; left: 17px; bottom: 20px;
    font-size: 19px; font-weight: 700; color: var(--accent);
  }
  .add-to-cart {
    position: absolute; right: 17px; bottom: 20px; width: 83px; height: 23px;
    background: var(--accent); color: var(--white); border: 0;
    font-family: inherit; font-size: 8px; font-weight: 800; letter-spacing: .2px;
  }
  .photo-lettuce { background: linear-gradient(135deg, #c7dd9a, #8fb55a 55%, #5f7f3a); }
  .photo-oyster { background: linear-gradient(135deg, #8a5a34, #c08a4f 50%, #4e3320); }
  .photo-shiitake { background: linear-gradient(135deg, #9a4a22, #4a2a1c 55%, #c5752f); }
  .photo-bean { background: linear-gradient(135deg, #6b4a2e, #5fa23a 40%, #7dbb4b 75%, #5a3a24); }
  .photo-eryngii { background: linear-gradient(135deg, #5a3b22, #e1b14a 45%, #c88a34); }
  .photo-potato { background: linear-gradient(135deg, #b7d08b, #86ad55 55%, #6c8b44); }
  .photo-soya { background: linear-gradient(135deg, #6e4a28, #e2c062 45%, #b88a3a); }
  .photo-corn { background: linear-gradient(135deg, #6a4526, #f0c43c 45%, #d99b28); }
  .photo-toast { background: linear-gradient(135deg, #b9733a, #e3a75a 50%, #8a4e24); }
</style>
</head>
<body>
  <aside class="sidebar">
    <div class="brand">TAVROZI</div>
    <ul class="category-nav">
      <li class="category-item is-active" style="top:92px"><svg viewBox="0 0 26 26" fill="none" stroke="#fff" stroke-width="1.6"><path d="M6 5l14 16M20 5L6 21M4 9c3-1 5 1 5 3M22 9c-3-1-5 1-5 3"/></svg>Vegetable</li>
      <li class="category-item" style="top:158px"><svg viewBox="0 0 26 26" fill="none" stroke="#fff" stroke-width="1.6"><ellipse cx="13" cy="13" rx="10" ry="7"/><circle cx="9" cy="13" r="2"/></svg>Meat</li>
      <li class="category-item" style="top:223px"><svg viewBox="0 0 26 26" fill="none" stroke="#fff" stroke-width="1.6"><path d="M18 4c-6 1-11 6-11 12 0 3 2 6 5 6M12 22l-3 2M18 4l3-1"/></svg>Seafood</li>
      <li class="category-item" style="top:288px"><svg viewBox="0 0 26 26" fill="none" stroke="#fff" stroke-width="1.6"><rect x="4" y="14" width="18" height="8" rx="2"/><path d="M8 14V7h6v7M16 10h4"/></svg>Special</li>
      <li class="category-item" style="top:352px"><svg viewBox="0 0 26 26" fill="none" stroke="#fff" stroke-width="1.6"><path d="M3 19h20M5 17a8 8 0 0116 0M13 7v2"/></svg>Cold Dish</li>
      <li class="category-item" style="top:415px"><svg viewBox="0 0 26 26" fill="none" stroke="#fff" stroke-width="1.6"><circle cx="13" cy="13" r="10"/><path d="M10 7v12M16 7v12"/></svg>Main</li>
      <li class="category-item" style="top:480px"><svg viewBox="0 0 26 26" fill="none" stroke="#fff" stroke-width="1.6"><circle cx="13" cy="13" r="10"/><path d="M7 19L19 7M9 10l7 7"/></svg>Set</li>
      <li class="category-item" style="top:544px"><svg viewBox="0 0 26 26" fill="none" stroke="#fff" stroke-width="1.6"><path d="M6 12h14l-2 11H8zM13 12V4l4-1"/></svg>Juice</li>
      <li class="category-item" style="top:610px"><svg viewBox="0 0 26 26" fill="none" stroke="#fff" stroke-width="1.6"><path d="M5 4h6l-1 8a2 2 0 01-4 0zM15 4h6l-1 8a2 2 0 01-4 0zM8 14v8M18 14v8M5 22h6M15 22h6"/></svg>Drink</li>
      <li class="category-item" style="top:678px"><svg viewBox="0 0 26 26" fill="none" stroke="#fff" stroke-width="1.6"><rect x="5" y="7" width="12" height="16" rx="1"/><path d="M17 10h3v8h-3M5 7c0-3 12-3 12 0"/></svg>Beer</li>
      <li class="category-item" style="top:740px"><svg viewBox="0 0 26 26" fill="none" stroke="#fff" stroke-width="1.6"><rect x="5" y="10" width="16" height="13" rx="3"/><path d="M9 10V6h8v4M10 3h6"/></svg>Alcohol</li>
      <li class="category-item" style="top:807px"><svg viewBox="0 0 26 26" fill="none" stroke="#fff" stroke-width="1.6"><path d="M8 3h10l-1 8a4 4 0 01-8 0zM13 15v7M9 22h8"/></svg>Wine</li>
    </ul>
  </aside>

  <h1 class="page-title">Vegetable</h1>
  <svg class="cart-button" viewBox="0 0 40 32" fill="none" stroke="#fff" stroke-width="2" stroke-linejoin="round" aria-label="Cart"><path d="M2 4h5l4 16h17l4-11H9"/><circle cx="13" cy="26" r="2.2"/><circle cx="26" cy="26" r="2.2"/></svg>
  <div class="cart-badge">02</div>

  <main class="dish-grid">
    <article class="dish-card"><div class="dish-photo photo-lettuce" role="img" aria-label="Grilled romaine lettuce skewers"></div><div class="dish-info"><h2 class="dish-name">Grilled Romaine Lettuce</h2><p class="dish-sub">烤油麦菜</p><p class="dish-price">S$1.30</p><button class="add-to-cart">ADD TO CART</button></div></article>
    <article class="dish-card"><div class="dish-photo photo-oyster" role="img" aria-label="Grilled oyster mushroom skewers"></div><div class="dish-info"><h2 class="dish-name">Grilled Oyster Mushroom</h2><p class="dish-sub">烤鲜耗菇</p><p class="dish-price">S$1.30</p><button class="add-to-cart">ADD TO CART</button></div></article>
    <article class="dish-card"><div class="dish-photo photo-shiitake" role="img" aria-label="Grilled shiitake mushroom skewers"></div><div class="dish-info"><h2 class="dish-name">烤香菇</h2><p class="dish-sub">Grilled Shitake Mushroom</p><p class="dish-price">S$1.30</p><button class="add-to-cart">ADD TO CART</button></div></article>
    <article class="dish-card"><div class="dish-photo photo-bean" role="img" aria-label="Grilled string bean skewers"></div><div class="dish-info"><h2 class="dish-name">Grilled String Bean</h2><p class="dish-sub">烤四季豆</p><p class="dish-price">S$1.30</p><button class="add-to-cart">ADD TO CART</button></div></article>
    <article class="dish-card"><div class="dish-photo photo-eryngii" role="img" aria-label="Grilled king oyster mushroom slices"></div><div class="dish-info"><h2 class="dish-name">Grilled Pleurotus Eryngii</h2><p class="dish-sub">烤杏鲍菇</p><p class="dish-price">S$1.30</p><button class="add-to-cart">ADD TO CART</button></div></article>
    <article class="dish-card"><div class="dish-photo photo-potato" role="img" aria-label="Grilled vegetable skewers"></div><div class="dish-info"><h2 class="dish-name">Grilled Potato Chip 3Pcs</h2><p class="dish-sub">烤土豆片 3pcs</p><p class="dish-price">S$2.60</p><button class="add-to-cart">ADD TO CART</button></div></article>
    <article class="dish-card"><div class="dish-photo photo-soya" role="img" aria-label="Grilled dry soya bean cake strips"></div><div class="dish-info"><h2 class="dish-name">Grilled Dry Soya Bean Cake 3Pcs</h2></div></article>
    <article class="dish-card"><div class="dish-photo photo-corn" role="img" aria-label="Grilled corn skewers"></div><div class="dish-info"><h2 class="dish-name">Grilled Romaine Lettuce</h2><p class="dish-sub">烤油麦菜</p></div></article>
    <article class="dish-card"><div class="dish-photo photo-toast" role="img" aria-label="Grilled bread slices"></div><div class="dish-info"><h2 class="dish-name">Grilled Romaine Lettuce</h2></div></article>
  </main>
</body>
</html>
```